Building Maintenance Flyer specialising in hot and silent pressure cleaning

Hi. I love this flyer. I would like something similar but with hot water pressure washing and building maintenance

Tidal Crest & Services provides high pressure steam cleaning and water blasting services throughout Brisbane and surrounding areas, covering the Industrial, Commercial, Strata and Residential property owners sectors.

TCS combining the cleaning power of heat with state-of-the-art silent equipment, accredited technicians and a steadfast commitment to the environment. We offer the best Prompt, Professional Service.

Fully Accredited & Certified Technicians
100% Satisfaction Guaranteed
We are a family owned and operated business and love what we do. No job is too big or too small and we take pride in our work.
All of our services are undertaken using industry leading equipment and, providing safe and superior results.

Our business is covered by 20 million full public liability insurance and we operate within strict health & safety guidelines, providing all our clients with complete peace of mind. Project plans and risk assessments can also be provided upon request.

BODY CORPORATES

BUILDING FAÇADE CLEANING

CAR PARKS – underground, single and multi level

DRIVE THRU

FOOD PRODUCTION FACILITIES CLEANING SANITISING

SHOPPING CENTRES

BIRD MANAGEMENT AND DECONTAMINATION

GENERAL MAINTENANCE

CONSTRUCTION CLEAN UPS

SPILL MANAGEMENT

CONCRETE CLEANING AND DEGRASING

CONCRETE SEALING

FACTORY CLEANING & CLEAN UP

ENVIRONMENTAL DECONTAMINATION OF HEAVY VEHICLES AND EQUIPMENT

SITE CLEANS AND RUBBISH REMOVAL

MANUFACTURING PLANTS

Target Market(s)

Facility Managers, Commercial and Industrial Property Owners, Property Managers, Schools, Restaurants,

Industry/Entity Type

Pressure Cleaning

Font styles to use
Sans Serif

Colors
0293ce
00a990
33a6d7
33b8a4

Requirements
Must have
• SILENT HOT WATER PRESSURE CLEANING
Runs up to 120 Degrees Celsius
SANITISING - Bin areas, outdoor areas, cafe's, restaurants, schools, drive thru's
Blue's and Greens to link in with our logo

```html
<!DOCTYPE html>
<html lang="en">
<head>
<meta charset="utf-8">
<title>Tidal Crest &amp; Services – Property Maintenance Flyer</title>
<link rel="stylesheet" href="https://fonts.googleapis.com/css2?family=Open+Sans:ital,wght@0,400;0,600;0,700;0,800;1,700;1,800&display=swap">
<style>
  :root {
    --navy: #1f4fa3;
    --royal: #2561b8;
    --sky: #0293ce;
    --sky-soft: #33a6d7;
    --teal: #00a990;
    --teal-soft: #33b8a4;
    --ink: #1b2a4a;
    --white: #ffffff;
    --mist: #e6ebf2;
  }
  * { box-sizing: border-box; margin: 0; padding: 0; }
  html, body { width: 1200px; height: 862px; overflow: hidden; background: #f2f2f2; }
  body { font-family: "Open Sans", Arial, sans-serif; }
  .flyer { position: relative; width: 1200px; height: 862px; background: var(--white); overflow: hidden; }
  .backdrop { position: absolute; inset: 0; }
  .abs { position: absolute; }

  .brand { left: 780px; top: 50px; width: 300px; display: flex; align-items: center; justify-content: center; gap: 12px; }
  .brand-dot { width: 22px; height: 22px; border-radius: 50%; background: var(--teal); }
  .brand-name { font-weight: 800; font-size: 30px; color: var(--navy); letter-spacing: 0.5px; line-height: 1; }
  .brand-full { left: 780px; top: 92px; width: 300px; text-align: center; font-size: 11px; font-weight: 700; color: var(--navy); letter-spacing: 1.5px; }

  .headline { left: 640px; top: 214px; width: 540px; text-align: center; font-weight: 800; font-style: italic; font-size: 38px; line-height: 45px; color: var(--royal); }
  .sectors { left: 640px; top: 372px; width: 540px; text-align: center; font-weight: 700; font-size: 20px; line-height: 31px; color: var(--teal-soft); }
  .rule { left: 652px; top: 456px; width: 510px; height: 2px; background: var(--ink); }
  .feature { left: 650px; top: 466px; width: 520px; font-style: italic; font-weight: 800; color: var(--royal); }
  .feature-title { font-size: 25px; line-height: 32px; }
  .feature-sub { font-size: 22px; line-height: 30px; }

  .checks { left: 642px; top: 556px; list-style: none; }
  .checks li { display: flex; align-items: center; gap: 11px; font-size: 17px; font-weight: 600; color: var(--royal); height: 31px; }
  .tick { width: 19px; height: 19px; flex: none; }

  .badge { left: 1012px; top: 552px; width: 172px; height: 172px; }
  .badge-text { left: 1012px; top: 601px; width: 172px; text-align: center; color: var(--royal); }
  .badge-big { font-size: 44px; font-weight: 800; line-height: 48px; }
  .badge-small { font-size: 12px; font-weight: 700; line-height: 16px; }

  .phone-row { left: 650px; top: 756px; display: flex; align-items: center; gap: 12px; }
  .phone-icon { width: 44px; height: 44px; }
  .phone-number { font-size: 52px; font-weight: 800; color: var(--royal); line-height: 1; letter-spacing: 1px; }
  .website { left: 702px; top: 818px; font-size: 19px; font-weight: 800; color: var(--ink); }

  .solutions-title { left: 104px; top: 534px; font-size: 28px; font-weight: 800; color: var(--white); letter-spacing: 0.5px; }
  .solutions { left: 54px; top: 598px; width: 470px; display: grid; grid-template-columns: 210px 220px; row-gap: 20px; list-style: none; }
  .solutions li { display: flex; align-items: center; gap: 12px; color: var(--white); font-size: 16px; font-weight: 600; line-height: 20px; min-height: 44px; }
  .sol-icon { width: 34px; height: 34px; flex: none; }
</style>
</head>
<body>
<main class="flyer">
  <svg class="backdrop" width="1200" height="862" viewBox="0 0 1200 862">
    <defs>
      <linearGradient id="bandGrad" x1="0" y1="0" x2="1" y2="0">
        <stop offset="0" stop-color="#2561b8"/>
        <stop offset="1" stop-color="#0293ce"/>
      </linearGradient>
      <linearGradient id="panelGrad" x1="0" y1="0" x2="0" y2="1">
        <stop offset="0" stop-color="#2561b8"/>
        <stop offset="1" stop-color="#173c85"/>
      </linearGradient>
      <linearGradient id="photoGrad" x1="0" y1="0" x2="1" y2="1">
        <stop offset="0" stop-color="#6f8a5a"/>
        <stop offset="0.55" stop-color="#9aa4a8"/>
        <stop offset="1" stop-color="#c7ccd0"/>
      </linearGradient>
      <linearGradient id="fadeGrad" x1="0" y1="0" x2="0" y2="1">
        <stop offset="0" stop-color="#ffffff"/>
        <stop offset="1" stop-color="#e3e8ef"/>
      </linearGradient>
    </defs>

    <!-- hero photo area -->
    <rect role="img" aria-label="Photo: technician in blue boots using a pressure washer wand on paving beside garden plants" x="0" y="0" width="760" height="600" fill="url(#photoGrad)"/>

    <!-- white content area with soft lower fade -->
    <path d="M720 0 H1200 V862 H610 C590 760 578 640 572 480 C560 300 610 140 720 0 Z" fill="url(#fadeGrad)"/>
    <!-- light swoosh along the curve -->
    <path d="M690 0 H722 C612 140 562 300 574 480 L548 500 C534 300 584 140 690 0 Z" fill="#e6ebf2"/>

    <!-- bottom right wave -->
    <path d="M780 862 C960 850 1100 790 1200 690 V862 Z" fill="url(#bandGrad)"/>
    <path d="M860 862 C1000 850 1120 800 1200 740 V760 C1120 820 1010 856 900 862 Z" fill="#ffffff" opacity="0.35"/>
    <path d="M700 862 C900 842 1060 780 1200 660 V676 C1060 796 900 852 740 862 Z" fill="#33a6d7" opacity="0.55"/>

    <!-- solutions panel -->
    <path d="M0 500 C160 470 360 470 480 520 C520 620 540 760 560 862 H0 Z" fill="url(#panelGrad)"/>
    <!-- light band beside panel -->
    <path d="M480 520 L506 512 C546 620 566 760 588 862 H560 C540 760 520 620 480 520 Z" fill="#dfe5ee"/>
    <!-- dark accent arc -->
    <path d="M548 470 C592 560 612 650 606 760 C596 660 578 570 530 486 Z" fill="#2b3140"/>

    <!-- round photos -->
    <circle cx="245" cy="392" r="78" fill="#ffffff"/>
    <circle role="img" aria-label="Photo: worker in orange hi-vis cleaning a shiny concrete floor" cx="245" cy="392" r="71" fill="#8e9aa3"/>
    <circle cx="452" cy="456" r="98" fill="#ffffff"/>
    <circle role="img" aria-label="Photo: trailer-mounted hot water pressure cleaning unit under trees" cx="452" cy="456" r="91" fill="#4d5a4c"/>
  </svg>

  <div class="abs brand"><span class="brand-dot"></span><span class="brand-name">TCS</span></div>
  <div class="abs brand-full">TIDAL CREST &amp; SERVICES</div>

  <h1 class="abs headline">ALL COMMERCIAL &amp;<br>INDUSTRIAL PROPERTY<br>MAINTENACE</h1>
  <p class="abs sectors">SANITISING BIN AREAS, OUTDOOR AREAS, CAFE'S,<br>RESTAURANTS, SCHOOLS, DRIVE THRU'S</p>
  <div class="abs rule"></div>
  <div class="abs feature">
    <div class="feature-title">SILENT HOT WATER PRESSURE CLEANING</div>
    <div class="feature-sub">Runs up to 120 Degrees Celsius</div>
  </div>

  <ul class="abs checks">
    <li><svg class="tick" viewBox="0 0 20 20"><rect width="20" height="20" rx="2" fill="#2561b8"/><path d="M4 10 L8.5 14.5 L16 5" stroke="#fff" stroke-width="3" fill="none"/></svg>Fully Accredited &amp; Certified Technicians</li>
    <li><svg class="tick" viewBox="0 0 20 20"><rect width="20" height="20" rx="2" fill="#2561b8"/><path d="M4 10 L8.5 14.5 L16 5" stroke="#fff" stroke-width="3" fill="none"/></svg>100% Satisfaction Guaranteed</li>
    <li><svg class="tick" viewBox="0 0 20 20"><rect width="20" height="20" rx="2" fill="#2561b8"/><path d="M4 10 L8.5 14.5 L16 5" stroke="#fff" stroke-width="3" fill="none"/></svg>Family owned and operated business</li>
    <li><svg class="tick" viewBox="0 0 20 20"><rect width="20" height="20" rx="2" fill="#2561b8"/><path d="M4 10 L8.5 14.5 L16 5" stroke="#fff" stroke-width="3" fill="none"/></svg>No job is too big or too small</li>
  </ul>

  <svg class="abs badge" viewBox="0 0 180 180" aria-hidden="true">
    <circle cx="90" cy="90" r="88" fill="#ffffff"/>
    <circle cx="90" cy="90" r="84" fill="none" stroke="#2561b8" stroke-width="4"/>
    <circle cx="90" cy="90" r="58" fill="none" stroke="#2561b8" stroke-width="3"/>
    <defs>
      <path id="arcTop" d="M22 90 A68 68 0 0 1 158 90"/>
      <path id="arcBottom" d="M18 92 A72 72 0 0 0 162 92"/>
    </defs>
    <text font-family="Open Sans, Arial, sans-serif" font-size="14" font-weight="800" fill="#2561b8" letter-spacing="1"><textPath href="#arcTop" startOffset="50%" text-anchor="middle">READY TO RESPOND</textPath></text>
    <text font-family="Open Sans, Arial, sans-serif" font-size="14" font-weight="800" fill="#2561b8" letter-spacing="1"><textPath href="#arcBottom" startOffset="50%" text-anchor="middle">READY TO RESPOND</textPath></text>
  </svg>
  <div class="abs badge-text">
    <div class="badge-small">24 HOURS</div>
    <div class="badge-big">24/7</div>
    <div class="badge-small">7 DAYS</div>
  </div>

  <div class="abs phone-row">
    <svg class="phone-icon" viewBox="0 0 46 46" aria-hidden="true">
      <circle cx="23" cy="23" r="20" fill="none" stroke="#2561b8" stroke-width="4"/>
      <path d="M13 14 C13 26 20 33 32 33 L33 28 L28 26 L26 28 C22 26 20 24 18 20 L20 18 L18 13 Z" fill="#2561b8"/>
    </svg>
    <span class="phone-number">1300 555 018</span>
  </div>
  <div class="abs website">www.tidalcrestservices.au</div>

  <h2 class="abs solutions-title">SOLUTIONS FOR:</h2>
  <ul class="abs solutions">
    <li><svg class="sol-icon" viewBox="0 0 34 34"><circle cx="17" cy="17" r="9" fill="#33b8a4"/><g stroke="#33b8a4" stroke-width="3"><path d="M17 2v6M17 26v6M2 17h6M26 17h6M6 6l4 4M24 24l4 4M28 6l-4 4M6 28l4-4"/></g></svg>COVID-19<br>Infection Control</li>
    <li><svg class="sol-icon" viewBox="0 0 34 34"><circle cx="12" cy="12" r="7" fill="#33b8a4"/><circle cx="24" cy="16" r="5" fill="#33b8a4"/><circle cx="15" cy="25" r="6" fill="#33b8a4"/></svg>Common Area<br>Cleaning</li>
    <li><svg class="sol-icon" viewBox="0 0 34 34"><rect x="4" y="8" width="26" height="22" fill="none" stroke="#33b8a4" stroke-width="3"/><path d="M4 16h26M4 23h26M13 8v22M21 8v22" stroke="#33b8a4" stroke-width="2"/></svg>Building<br>Management</li>
    <li><svg class="sol-icon" viewBox="0 0 34 34"><path d="M4 18 C10 10 18 12 22 16 L30 10 L26 20 C22 26 12 26 4 18 Z" fill="#33b8a4"/></svg>Bird waste<br>removal</li>
    <li><svg class="sol-icon" viewBox="0 0 34 34"><rect x="6" y="6" width="22" height="4" fill="#33b8a4"/><path d="M8 12h18l-2 18H10Z" fill="#33b8a4"/></svg>Bin Cleaning &amp;<br>Sanitisation</li>
    <li><svg class="sol-icon" viewBox="0 0 34 34"><circle cx="17" cy="17" r="8" fill="#33b8a4"/><g fill="#33b8a4"><circle cx="6" cy="8" r="3"/><circle cx="28" cy="9" r="3"/><circle cx="7" cy="27" r="3"/><circle cx="27" cy="26" r="3"/></g></svg>Mould &amp; Mildew<br>removal</li>
    <li><svg class="sol-icon" viewBox="0 0 34 34"><path d="M4 30h26M9 30V12M17 30V6M25 30V14" stroke="#33b8a4" stroke-width="3"/><path d="M9 12l-4-4M17 6l4-3M25 14l4-4" stroke="#33b8a4" stroke-width="3"/></svg>Garden<br>Maintenance</li>
    <li><svg class="sol-icon" viewBox="0 0 34 34"><rect x="8" y="8" width="18" height="22" rx="3" fill="#33b8a4"/><rect x="12" y="3" width="10" height="5" fill="#33b8a4"/></svg>Oil and Grease<br>elimination</li>
  </ul>
</main>
</body>
</html>
```